Tellwick Asset Management - Corporate Letter Head Project

Looking for a classy design based on our current logo. Please find current logo source file in files. With our color scheme.

Target Market(s)

We're an investment firm, the letterhead needs to look professional and attractive to clients.

Industry/Entity Type

Hedgefund

Colors
0054AA
0677BA
7BADD7
CADEEF
E8F1F8

Requirements
Must have
• Our logo, address, phone number, and email

```html
<!DOCTYPE html>
<html lang="en">
<head>
<meta charset="utf-8">
<title>Tellwick Asset Management – Letterhead</title>
<link href="https://fonts.googleapis.com/css2?family=Open+Sans:wght@400;600;700&display=swap" rel="stylesheet">
<style>
  :root {
    --navy: #0b2a56;
    --ink: #222222;
    --body: #5b5b5b;
    --muted: #6a6a6a;
    --rule: #dcdcdc;
    --band-grey: #cfcfcf;
    --paper: #ffffff;
  }
  * { margin: 0; padding: 0; box-sizing: border-box; }
  html, body { width: 922px; height: 1200px; overflow: hidden; background: var(--paper); }
  body { font-family: "Open Sans", Arial, sans-serif; color: var(--ink); }
  .letterhead { position: relative; width: 922px; height: 1200px; background: var(--paper); }

  .brand { position: absolute; left: 68px; top: 76px; display: flex; align-items: center; gap: 16px; }
  .brand-mark { width: 68px; height: 74px; border: 2px solid var(--navy); }
  .brand-name { color: var(--navy); font-weight: 600; text-transform: uppercase; line-height: 1; }
  .brand-name .line-1 { display: block; font-size: 27px; letter-spacing: 0.5px; }
  .brand-name .line-2 { display: block; font-size: 13px; letter-spacing: 9.4px; margin-top: 6px; }

  .contact { position: absolute; right: 68px; top: 56px; text-align: right; font-size: 12px; color: var(--muted); }
  .contact-row { display: flex; justify-content: flex-end; align-items: flex-start; gap: 6px; margin-bottom: 9px; line-height: 15px; }
  .contact-row svg { flex: none; width: 17px; height: 17px; }

  .header-rule { position: absolute; left: 56px; top: 194px; width: 798px; height: 10px; }

  .recipient { position: absolute; left: 68px; top: 320px; }
  .recipient-name { font-size: 21px; font-weight: 600; color: var(--navy); line-height: 28px; }
  .recipient-title { font-size: 12px; color: var(--ink); margin-bottom: 8px; }
  .recipient-line { font-size: 14.5px; line-height: 25px; }
  .recipient-line b { color: var(--navy); display: inline-block; width: 30px; font-weight: 700; }

  .letter-date { position: absolute; right: 74px; top: 420px; font-size: 14.5px; }

  .letter-body { position: absolute; left: 68px; top: 495px; width: 780px; font-size: 14.5px; color: var(--body); }
  .letter-body p { margin-bottom: 31px; }
  .letter-body span { display: block; white-space: nowrap; overflow: hidden; line-height: 31px; }

  .sign-off { position: absolute; left: 648px; top: 896px; width: 180px; text-align: center; }
  .signature { width: 160px; height: 42px; margin: 0 auto 4px; background: linear-gradient(90deg, #f4f4f4, #e8e8e8, #f4f4f4); }
  .signer-name { font-size: 15px; font-weight: 700; line-height: 19px; }
  .signer-role { font-size: 14px; line-height: 18px; }

  .footer-band { position: absolute; left: 0; bottom: 0; width: 922px; height: 16px; }
</style>
</head>
<body>
<main class="letterhead">

  <div class="brand">
    <div class="brand-mark"></div>
    <div class="brand-name">
      <span class="line-1">Tellwick Asset</span>
      <span class="line-2">Management</span>
    </div>
  </div>

  <address class="contact" style="font-style: normal;">
    <div class="contact-row">
      <span>2710 Harlow Crescent<br>Fairmont, VA 22310</span>
      <svg viewBox="0 0 17 17"><rect width="17" height="17" rx="3" fill="#0b2a56"/><path d="M8.5 3.5a3.3 3.3 0 0 0-3.3 3.3c0 2.5 3.3 6.2 3.3 6.2s3.3-3.7 3.3-6.2a3.3 3.3 0 0 0-3.3-3.3zm0 4.5a1.2 1.2 0 1 1 0-2.4 1.2 1.2 0 0 1 0 2.4z" fill="#fff"/></svg>
    </div>
    <div class="contact-row">
      <span>+00 555 018 42</span>
      <svg viewBox="0 0 17 17"><rect width="17" height="17" rx="3" fill="#0b2a56"/><path d="M5.2 4c.5-.3 1-.2 1.3.3l.9 1.6c.2.4.1.9-.3 1.2l-.6.4c.5 1.2 1.4 2.1 2.6 2.7l.4-.6c.3-.4.8-.5 1.2-.3l1.6.9c.5.3.6.8.3 1.3-.6 1-1.6 1.4-2.6 1.1C7.4 12 5 9.6 4.4 7 4.1 5.9 4.4 4.7 5.2 4z" fill="#fff"/></svg>
    </div>
    <div class="contact-row">
      <span>office@tellwickam.com</span>
      <svg viewBox="0 0 17 17"><rect width="17" height="17" rx="3" fill="#0b2a56"/><rect x="3.5" y="5" width="10" height="7" fill="none" stroke="#fff" stroke-width="1.2"/><path d="M3.5 5l5 4 5-4" fill="none" stroke="#fff" stroke-width="1.2"/></svg>
    </div>
    <div class="contact-row">
      <span>www.tellwickam.com</span>
      <svg viewBox="0 0 17 17"><rect width="17" height="17" rx="3" fill="#0b2a56"/><path d="M6 4l6 5.2-2.7.3 1.5 3-1.2.6-1.5-3L6 12z" fill="#fff"/></svg>
    </div>
  </address>

  <svg class="header-rule" viewBox="0 0 798 10" preserveAspectRatio="none">
    <rect x="0" y="4" width="798" height="2" fill="#dcdcdc"/>
    <polygon points="6,0 250,0 244,10 0,10" fill="#0b2a56"/>
  </svg>

  <section class="recipient">
    <div class="recipient-name">Martin Alder</div>
    <div class="recipient-title">Chief Director</div>
    <div class="recipient-line"><b>A :</b>12-4, Kestrel Road Lindham - 4417</div>
    <div class="recipient-line"><b>W :</b>m.alder@postbox.com, www.alderweb.com</div>
    <div class="recipient-line"><b>P :</b>+555 - 01928 - 3746</div>
  </section>

  <div class="letter-date">Date, 10 September, 2019</div>

  <article class="letter-body">
    <p>
      <span>This is a sample letter that has been placed to demonstrate typing remat (Your Company). letterhead</span>
      <span>design. When positioned properly, it will serve to work in harmony with all other elements letterhead.</span>
      <span>This letterhead design is meant to project an image</span>
    </p>
    <p>
      <span>This letterhead design is meant project an image of professionalism reliability. By using simple aligen</span>
      <span>we have created a very spacious feeling. The simplicity suggest&nbsp; rengththe spaciousnes contributes h</span>
      <span>aesthetics the layout. These basic qualities along with the (Your Company)</span>
    </p>
    <p>
      <span>look and helps reinforce the (Your Company) brand. letterhead design is meant to project an image p</span>
      <span>design. When positioned properly, it will serve to work in harmony all the other elements letterhead.</span>
      <span>sionalism and reliability.</span>
    </p>
  </article>

  <div class="sign-off">
    <div class="signature" role="img" aria-label="Handwritten signature of Peter Calloway"></div>
    <div class="signer-name">Peter Calloway</div>
    <div class="signer-role">Manager</div>
  </div>

  <svg class="footer-band" viewBox="0 0 922 16" preserveAspectRatio="none">
    <rect x="0" y="0" width="922" height="16" fill="#cfcfcf"/>
    <polygon points="0,0 644,0 636,16 0,16" fill="#0b2a56"/>
    <polygon points="644,0 650,0 642,16 636,16" fill="#ffffff"/>
  </svg>

</main>
</body>
</html>
```